Flyer for tutoring

The text should be presented in an engaging way to attract potential customers.
Colorfully designed
Around the edge, various objects related to school and the subjects (see text) should be visible.

```html
<!DOCTYPE html>
<html lang="de">
<head>
<meta charset="utf-8">
<title>Nachhilfe Flyer</title>
<link rel="stylesheet" href="https://fonts.googleapis.com/css2?family=Bebas+Neue&family=Montserrat:wght@300;400;600;700;800&display=swap">
<style>
  :root {
    --purple: #6a2d8c;
    --purple-soft: #7b4fa8;
    --yellow: #ffe500;
    --gold: #ffc800;
    --red: #e2000f;
    --sky: #5cc3e6;
    --ink: #1d1d1d;
    --white: #ffffff;
  }
  * { margin: 0; padding: 0; box-sizing: border-box; }
  html, body { width: 726px; height: 1200px; overflow: hidden; background: #e6e6e6; }
  .flyer {
    position: relative; width: 726px; height: 1200px; overflow: hidden;
    background: var(--white); font-family: "Montserrat", Arial, sans-serif; color: var(--ink);
  }
  .shapes { position: absolute; inset: 0; }
  .intro {
    position: absolute; top: 34px; left: 0; width: 100%; text-align: center;
    color: var(--white); font-weight: 300; font-size: 25px; line-height: 1.25;
  }
  .divider {
    position: absolute; top: 130px; left: 334px; width: 60px; height: 3px; background: var(--white);
  }
  .headline-kicker {
    position: absolute; top: 150px; left: 0; width: 100%; text-align: center;
    color: var(--gold); font-weight: 800; font-size: 47px; letter-spacing: 0.5px;
  }
  .headline {
    position: absolute; top: 210px; left: 0; width: 100%; text-align: center;
    font-family: "Bebas Neue", Impact, sans-serif; color: var(--white);
    font-size: 84px; line-height: 90px; font-weight: 400;
  }
  .headline .second { display: block; padding-left: 40px; }
  .tagline {
    position: absolute; top: 436px; left: 124px; width: 504px; height: 48px;
    background: var(--white); transform: rotate(-5.5deg); transform-origin: left top;
    color: var(--purple); font-weight: 700; font-size: 24px; line-height: 48px; padding-left: 20px;
  }
  .lesson-title {
    position: absolute; top: 604px; left: 53px; white-space: nowrap;
    font-family: "Bebas Neue", Impact, sans-serif; font-weight: 400;
    color: var(--purple); font-size: 25px; line-height: 28px;
  }
  .lesson-text {
    position: absolute; top: 642px; left: 53px; width: 600px; font-size: 13px; line-height: 17px;
  }
  .highlight {
    position: absolute; top: 728px; left: 53px; width: 560px; height: 60px;
    background: linear-gradient(90deg, var(--yellow) 0%, #fff59a 70%, rgba(255,255,255,0) 100%);
    font-weight: 700; font-size: 15.5px; line-height: 19px; padding: 10px 0 0 8px;
  }
  .promise {
    position: absolute; top: 804px; left: 55px; color: var(--red);
    font-weight: 700; font-size: 24.5px; line-height: 28px;
  }
  .photo {
    position: absolute; left: 380px; top: 868px; width: 346px; height: 272px;
    background: radial-gradient(ellipse at 58% 55%, #c9a27f 0%, #6e7fa8 45%, rgba(122,80,168,0.35) 80%, rgba(255,255,255,0) 100%);
  }
  .about {
    position: absolute; top: 890px; left: 56px; width: 300px; padding-left: 10px;
    border-left: 2px solid var(--purple); font-size: 12.6px; line-height: 15.5px;
  }
  .about strong { font-weight: 700; }
  .contact-title {
    position: absolute; top: 1022px; left: 54px; color: var(--red); font-weight: 700; font-size: 20px;
  }
  .contact-line {
    position: absolute; left: 54px; display: flex; align-items: center; gap: 3px;
  }
  .contact-line svg { width: 20px; height: 20px; }
  .contact-mail { top: 1058px; font-size: 21px; }
  .contact-phone { top: 1090px; font-size: 23px; font-weight: 700; color: var(--red); }
  .contact-phone small { font-size: 10px; font-weight: 400; color: var(--ink); margin-left: 4px; align-self: flex-end; padding-bottom: 4px; }
  .footer-band {
    position: absolute; left: 0; bottom: 0; width: 100%; height: 60px; background: var(--yellow);
    text-align: center; font-size: 21.5px; line-height: 60px;
  }
</style>
</head>
<body>
<div class="flyer">
  <svg class="shapes" width="726" height="1200" viewBox="0 0 726 1200">
    <path d="M0 0 H726 V440 L90 578 L72 580 Q 22 580 16 520 L0 380 Z" fill="var(--yellow)" transform="translate(0,6)"/>
    <path d="M0 0 H726 V440 L90 574 Q 30 580 18 520 L0 380 Z" fill="var(--purple)"/>
    <path d="M652 424 H726 V548 L615 585 Z" fill="var(--red)"/>
    <path d="M0 774 L46 790 L0 872 Z" fill="var(--sky)"/>
    <path d="M726 842 V1140 H520 Z" fill="var(--purple-soft)"/>
    <path d="M184 338 C 150 360 148 410 176 452" stroke="var(--yellow)" stroke-width="5" fill="none" stroke-linecap="round"/>
    <path d="M162 446 L184 462 L186 436 Z" fill="var(--yellow)"/>
  </svg>

  <p class="intro">Möchtest du dich gerne in der Schule<br>verbessern undsuchst eine</p>
  <div class="divider"></div>
  <p class="headline-kicker">PROFESSIONELLE</p>
  <h1 class="headline">NACHHILFELEHRERIN /<span class="second">LERNCOACH ?</span></h1>
  <p class="tagline">Dann lass es uns doch mal versuchen!</p>

  <div class="photo" role="img" aria-label="Foto: drei lachende Schüler mit Daumen hoch, Kopfhörern und gelbem Heft"></div>

  <h2 class="lesson-title">Die erste Lektion – die Kennenlernlektion – dauert ca. 30 Minuten.</h2>
  <p class="lesson-text">Sie ist kostenlos. Denn wir müssen ja sicher gehen, dass wir uns verstehen und leiden können. Bei unserem ersten Treffen legen wir auch fest, woran wir arbeiten werden und wann die Nachhilfe in deine Agenda passt.</p>
  <p class="highlight">Wenn der erste Eindruck stimmt, dann legen wir los,<br>und bald schon werden</p>
  <p class="promise">deine Motivation und<br>deine Noten besser und besser!</p>

  <p class="about"><strong>Zu meiner Person:</strong> Ich wohne hier in der Siedlung Lindenhof und bin ausgebildete und sehr erfahrene Sekundar- und Primarlehrerin in den Fächern Deutsch, Französisch, Englisch und Geschichte. (Auf Wunsch auch Mathe-Nachhilfe möglich.)</p>

  <p class="contact-title">Meine Kontaktdaten:</p>
  <p class="contact-line contact-mail">
    <svg viewBox="0 0 20 20" aria-hidden="true"><circle cx="10" cy="10" r="9" fill="none" stroke="#1d1d1d" stroke-width="1.6"/><rect x="5" y="6.5" width="10" height="7" fill="#1d1d1d"/><path d="M5 6.5 L10 10.5 L15 6.5" stroke="#fff" stroke-width="1" fill="none"/></svg>
    lena.vogt@mailpost.ch
  </p>
  <p class="contact-line contact-phone">
    <svg viewBox="0 0 20 20" aria-hidden="true"><circle cx="10" cy="10" r="9" fill="none" stroke="#1d1d1d" stroke-width="1.6"/><path d="M6.5 5 L8.5 5 L9.3 7.8 L8 8.8 Q 9.2 11.3 11.2 12 L12.2 10.7 L15 11.5 L15 13.5 Q 10 14.5 6 9 Q 5.5 6.5 6.5 5 Z" fill="#1d1d1d"/></svg>
    079 512 40 87<small>(nachmittags fast immer erreichbar)</small>
  </p>

  <p class="footer-band">Ich freue mich auf deine Kontaktaufnahme! Bis bald!</p>
</div>
</body>
</html>
```